Verdant Pathworks Business Card

want the back of card to be blue- with the logo in the center
front of card- info plus logo (info being mailing address, email address, and website address )
4 different names with titles to have on cards
1) Dominic Ashvale - Owner
2) Bethany Korvuth- Customer Relationship Specialist
3) Luca Brennwick- Vice President of Sales
4) Neil Umbright- Chief Technology Officer

Target Market(s)

tech company in the government/probation office industry

Industry/Entity Type

Government Office

Contact Information for Business Card

1) Dominic Ashvale - Owner

Colors
0355a3
ffffff

Requirements
Must have
• back side should be blue, with the logo placed in the center
• front side needs to include both the logo, as well as company info (info should include website address, email address, and mailing address)

```html
<!DOCTYPE html>
<html lang="en">
<head>
<meta charset="utf-8">
<title>Verdant Pathworks Business Cards</title>
<link href="https://fonts.googleapis.com/css2?family=Cinzel:wght@500&family=Cormorant+Garamond:wght@500&family=Open+Sans:wght@400&display=swap" rel="stylesheet">
<style>
  :root {
    --board: #858585;
    --paper: #ffffff;
    --navy: #1f2e5e;
    --navy-deep: #17295a;
    --strip: #8a8a8a;
    --soft: #a9b0c8;
    --ink-light: #d9dcea;
  }
  html, body { margin: 0; padding: 0; overflow: hidden; }
  body {
    width: 1200px; height: 1107px; background: var(--board);
    position: relative; font-family: "Open Sans", sans-serif;
  }
  .card {
    position: absolute; width: 325px; height: 200px; overflow: hidden;
    box-shadow: 10px 12px 16px rgba(0,0,0,0.45);
  }
  .front { left: 236px; background: var(--paper); }
  .back { left: 638px; background: var(--navy-deep); display: flex; align-items: center; justify-content: center; }
  .brand {
    font-family: "Cinzel", serif; font-weight: 500; color: var(--navy);
    text-align: center; letter-spacing: 0.5px; line-height: 1;
  }
  .front .brand {
    position: absolute; top: 38px; left: 0; right: 0; font-size: 21px;
  }
  .front .brand .mark {
    display: block; width: 20px; height: 20px; margin: 0 auto 8px;
    background: var(--navy);
  }
  .back .brand { color: var(--paper); font-size: 28px; }
  .back .brand .mark {
    display: block; width: 26px; height: 26px; margin: 0 auto 12px;
    background: var(--paper);
  }
  .info-band {
    position: absolute; top: 107px; left: 0; width: 100%; height: 57px;
    background: var(--navy);
  }
  .person {
    position: absolute; right: 173px; top: 15px; text-align: right; white-space: nowrap;
  }
  .person .name {
    font-family: "Cormorant Garamond", serif; font-weight: 500; color: var(--soft);
    font-size: 13.5px; letter-spacing: 1px; text-transform: uppercase; line-height: 1;
  }
  .person .title { font-size: 7.5px; color: var(--ink-light); margin-top: 2px; }
  .divider {
    position: absolute; left: 164px; top: 8px; width: 1px; height: 42px; background: var(--ink-light);
  }
  .contacts {
    position: absolute; left: 175px; top: 7px; margin: 0; padding: 0; list-style: none;
    font-size: 7.5px; color: var(--soft); line-height: 14px;
  }
  .contacts li { display: flex; align-items: center; gap: 5px; }
  .contacts svg { width: 6px; height: 6px; fill: var(--ink-light); }
  .address-strip {
    position: absolute; top: 164px; left: 0; width: 100%; height: 12px; background: var(--strip);
    display: flex; align-items: center; justify-content: center; gap: 4px;
    font-size: 7.5px; color: var(--paper);
  }
  .address-strip svg { width: 6px; height: 8px; fill: var(--navy); }
</style>
</head>
<body>

<svg width="0" height="0" style="position:absolute">
  <defs>
    <symbol id="icon-phone" viewBox="0 0 10 10"><path d="M2 0h2l1 3-1.5 1a6 6 0 0 0 2.5 2.5L7 5l3 1v2c0 1-1 2-2 2A8 8 0 0 1 0 2c0-1 1-2 2-2z"/></symbol>
    <symbol id="icon-mail" viewBox="0 0 10 10"><path d="M0 2h10v6H0z M0 2l5 3 5-3" /></symbol>
    <symbol id="icon-web" viewBox="0 0 10 10"><circle cx="5" cy="5" r="5"/></symbol>
    <symbol id="icon-pin" viewBox="0 0 8 10"><path d="M4 0a4 4 0 0 1 4 4c0 3-4 6-4 6S0 7 0 4a4 4 0 0 1 4-4zm0 2.5a1.5 1.5 0 1 0 0 3 1.5 1.5 0 0 0 0-3z"/></symbol>
  </defs>
</svg>

<!-- Front 1 -->
<div class="card front" style="top:97px">
  <div class="brand"><span class="mark"></span>Verdant Pathworks</div>
  <div class="info-band">
    <div class="person"><div class="name">Dominic Ashvale</div><div class="title">Owner</div></div>
    <div class="divider"></div>
    <ul class="contacts">
      <li><svg><use href="#icon-phone"/></svg>000 000 0000</li>
      <li><svg><use href="#icon-mail"/></svg>youremail@xyz.com</li>
      <li><svg><use href="#icon-web"/></svg>www.yourwebsite.com</li>
    </ul>
  </div>
  <div class="address-strip"><svg><use href="#icon-pin"/></svg>Your Address here</div>
</div>

<!-- Front 2 -->
<div class="card front" style="top:332px">
  <div class="brand"><span class="mark"></span>Verdant Pathworks</div>
  <div class="info-band">
    <div class="person"><div class="name">Bethany Korvuth</div><div class="title">Customer Relationship Specialist</div></div>
    <div class="divider"></div>
    <ul class="contacts">
      <li><svg><use href="#icon-phone"/></svg>000 000 0000</li>
      <li><svg><use href="#icon-mail"/></svg>youremail@xyz.com</li>
      <li><svg><use href="#icon-web"/></svg>www.yourwebsite.com</li>
    </ul>
  </div>
  <div class="address-strip"><svg><use href="#icon-pin"/></svg>Your Address here</div>
</div>

<!-- Front 3 -->
<div class="card front" style="top:569px">
  <div class="brand"><span class="mark"></span>Verdant Pathworks</div>
  <div class="info-band">
    <div class="person"><div class="name">Neil Umbright</div><div class="title">Chief Technology Officer</div></div>
    <div class="divider"></div>
    <ul class="contacts">
      <li><svg><use href="#icon-phone"/></svg>000 000 0000</li>
      <li><svg><use href="#icon-mail"/></svg>youremail@xyz.com</li>
      <li><svg><use href="#icon-web"/></svg>www.yourwebsite.com</li>
    </ul>
  </div>
  <div class="address-strip"><svg><use href="#icon-pin"/></svg>Your Address here</div>
</div>

<!-- Front 4 -->
<div class="card front" style="top:811px">
  <div class="brand"><span class="mark"></span>Verdant Pathworks</div>
  <div class="info-band">
    <div class="person"><div class="name">Luca Brennwick</div><div class="title">Vice President of Sales</div></div>
    <div class="divider"></div>
    <ul class="contacts">
      <li><svg><use href="#icon-phone"/></svg>000 000 0000</li>
      <li><svg><use href="#icon-mail"/></svg>youremail@xyz.com</li>
      <li><svg><use href="#icon-web"/></svg>www.yourwebsite.com</li>
    </ul>
  </div>
  <div class="address-strip"><svg><use href="#icon-pin"/></svg>Your Address here</div>
</div>

<!-- Backs -->
<div class="card back" style="top:97px"><div class="brand"><span class="mark"></span>Verdant Pathworks</div></div>
<div class="card back" style="top:335px"><div class="brand"><span class="mark"></span>Verdant Pathworks</div></div>
<div class="card back" style="top:573px"><div class="brand"><span class="mark"></span>Verdant Pathworks</div></div>
<div class="card back" style="top:811px"><div class="brand"><span class="mark"></span>Verdant Pathworks</div></div>

</body>
</html>
```